Cards & Invitations

Hi!
We would like you to design 3 amazing cards for us.
1. Wedding invitation.
We would like to have a spring wedding invitation. It has to be A4 folded to A5 format, floral theme, but made in a very classic style. It has to contain light green and blue colors, but you are free to use other colors as well.
Text to be included:
Mr. and Mrs. Delwyn Avercross
Request the honour of your presence
At the marriage of their daughter
Marisse Avercross
to
Owen Ralditch
Saturday, the eighteenth of April
Two thousand and twelve
At three o'clock in the afternoon
Saint Wendel's Church
58 Brindle Street,
South Hampton, New York
Followed by a dinner at
Restaurant Verlane, Osgood Road 347
R.S.V.P. by the ninth of April
2. Christening invitation in Vintage style.
We need an invitation for a christening of Nico Farrowby. We would like it to be in vintage style, in light pink or lilac color and containing the photo of the baby.
It should also have some church symbols, like cross, prayer beads etc (one element is enough, not all together). Format: A5 horisontal (landscape) card. Please, find the photo attached.
Text to be included:
You are invited to
Witness and Celebrate
the Baptism of our daughter
Nico Farrowby
Sunday, September 26th at 1 p.m.
St. Ambrel Church
5821 Lindqvist Row, Parktown
Reception following the ceremony
at the Farrowby home
7302 Harlowe, Pearl Sound
Please reply by September 18th
3. Birthday invitation.
This is an invitation for Nico's 7th birthday party. The theme is racing. It should contain his photo and a race car (cars) or racing competition. No color preferences. It's a square folded card. Please, find attached the photo.
Text on the outside: Nico is turning 7
Text on the inside:
You are invited to join us
for Nico's 7th Birthday Celebration
Saturday, September 18th
We will have the celebration at Blue Juniper,
486 Quillby Road, Federal Way
Please reply by September 7th
to Bram at 175-389-602
Welcome!

```html
<!DOCTYPE html>
<html lang="en">
<head>
<meta charset="utf-8">
<title>Christening invitation – Nico Farrowby</title>
<link href="https://fonts.googleapis.com/css2?family=Comic+Neue:wght@400;700&family=Didact+Gothic&display=swap" rel="stylesheet">
<style>
  :root {
    --pink-deep: #f070b2;
    --pink-mid: #f6a6cf;
    --pink-soft: #fbd3e6;
    --blush: #fde8f0;
    --hat-pink: #e98fb0;
    --skin: #f2c3b3;
    --skin-shade: #e3a596;
    --cream: #f5e2cc;
    --ink-magenta: #c81e8f;
    --ink-plum: #7d0a4c;
    --title-ice: #eefcff;
    --title-glow: #8fdcec;
    --panel-fill: rgba(255, 238, 247, 0.55);
    --panel-edge: rgba(228, 110, 175, 0.8);
    --vintage-shade: rgba(150, 70, 100, 0.18);
  }
  html, body {
    margin: 0;
    padding: 0;
    width: 1200px;
    height: 846px;
    overflow: hidden;
    background: #ffffff;
  }
  .invitation {
    position: relative;
    width: 1200px;
    height: 846px;
    overflow: hidden;
    background:
      radial-gradient(ellipse 560px 380px at 160px 200px, rgba(240, 80, 165, 0.6), transparent 72%),
      radial-gradient(ellipse 720px 520px at 1080px 720px, rgba(205, 140, 170, 0.45), transparent 70%),
      linear-gradient(135deg, var(--pink-deep) 0%, var(--pink-mid) 30%, var(--pink-soft) 60%, var(--blush) 100%);
    font-family: "Didact Gothic", "Century Gothic", sans-serif;
  }
  .vintage-vignette {
    position: absolute;
    inset: 0;
    pointer-events: none;
    box-shadow: inset 0 0 120px 30px var(--vintage-shade);
  }
  .baby-photo {
    position: absolute;
    left: 0;
    top: 330px;
    width: 660px;
    height: 516px;
    background:
      radial-gradient(ellipse 190px 150px at 250px 280px, var(--skin) 0%, var(--skin-shade) 70%, transparent 100%),
      radial-gradient(ellipse 200px 120px at 470px 230px, var(--skin) 0%, transparent 100%),
      radial-gradient(ellipse 260px 170px at 190px 120px, var(--hat-pink) 0%, rgba(233, 143, 176, 0.6) 60%, transparent 100%),
      radial-gradient(ellipse 120px 230px at 570px 280px, rgba(233, 143, 176, 0.85) 0%, transparent 100%),
      radial-gradient(ellipse 420px 180px at 300px 470px, var(--cream) 0%, transparent 100%),
      linear-gradient(180deg, rgba(245, 185, 200, 0.7), rgba(245, 215, 205, 0.9));
    -webkit-mask-image: radial-gradient(ellipse 340px 300px at 320px 270px, #000 70%, transparent 100%);
    mask-image: radial-gradient(ellipse 340px 300px at 320px 270px, #000 70%, transparent 100%);
  }
  .title {
    position: absolute;
    left: 41px;
    top: 50px;
    margin: 0;
    font-family: "Comic Neue", "Comic Sans MS", cursive;
    font-weight: 400;
    font-size: 58px;
    line-height: 70px;
    letter-spacing: 3px;
    color: var(--title-ice);
    text-shadow: 0 0 6px var(--title-glow), 0 0 2px #5fc6dc;
  }
  .details-panel {
    position: absolute;
    left: 603px;
    top: 135px;
    width: 536px;
    height: 671px;
    box-sizing: border-box;
    border: 2px solid var(--panel-edge);
    border-radius: 6px;
    background: var(--panel-fill);
  }
  .church-cross {
    position: absolute;
    right: 22px;
    top: 20px;
    width: 22px;
    height: 32px;
  }
  .invite-lead {
    position: absolute;
    left: 32px;
    top: 38px;
    margin: 0;
    font-size: 26px;
    line-height: 34px;
    color: var(--ink-magenta);
  }
  .child-name {
    position: absolute;
    left: 94px;
    top: 178px;
    margin: 0;
    font-family: "Comic Neue", "Comic Sans MS", cursive;
    font-weight: 700;
    font-size: 58px;
    line-height: 70px;
    color: var(--ink-plum);
  }
  .ceremony, .reception {
    position: absolute;
    left: 0;
    width: 550px;
    margin: 0;
    text-align: center;
    font-size: 26px;
    line-height: 34px;
    color: var(--ink-magenta);
  }
  .ceremony { top: 309px; }
  .reception { top: 479px; }
  .reception-heading { text-decoration: underline; text-underline-offset: 4px; }
</style>
</head>
<body>
  <main class="invitation">
    <div class="baby-photo" role="img" aria-label="Photo of the sleeping baby girl in a pink knitted hat on a cream blanket"></div>
    <div class="vintage-vignette"></div>
    <h1 class="title">Christening invitation</h1>
    <section class="details-panel">
      <svg class="church-cross" viewBox="0 0 22 32" aria-hidden="true">
        <rect x="9" y="0" width="4" height="32" fill="#c81e8f" opacity="0.55"/>
        <rect x="2" y="8" width="18" height="4" fill="#c81e8f" opacity="0.55"/>
      </svg>
      <p class="invite-lead">You are invited to,<br>Witness and Celebrate<br>the Baptism of our daughter</p>
      <h2 class="child-name">Nico Farrowby</h2>
      <p class="ceremony">Sunday, September 26th at 1 p.m.<br>St. Ambrel Church<br>5821 Lindqvist Row, Parktown</p>
      <p class="reception"><span class="reception-heading">Reception following the ceremony</span><br>at the Farrowby home<br>7302 Harlowe, Pearl Sound<br>Please reply by September 18th</p>
    </section>
  </main>
</body>
</html>
```